Business Card Design needed - Something Awesome!

Need a business card designed. Company is "Harbor Vane Consulting" we do consulting and also have sales automation technology.
I'm going to use thick stock or metal, something really nice... I was thinking about a QR Code on the back that would just upload my contact info to the persons contact, etc -

This is a Strategy Company with a tech feel. I'm open to ideas but really want this to be nice!

I need a template that should include:

Name | Position or Title
D: 555.203.8146
www.harborvaneconsulting.example

I'm going to attach my contact so you can use that one, I need to get this printed.

Target Market(s)

Small to mid size customers, Entrepreneurs etc.

Industry/Entity Type

Consulting, Tech, Private Equity.

Contact Information for Business Card

Name, Phone, Maybe email, URL

Font styles to use
Sans Serif

Colors

Designer to choose only greyscale colors for use in the design.

Requirements
Must have
• Fresh, Clean, stand out from the crowd - will be on thick stock or metal.
Nice to have
• Clean, simple yet impactful.
Should not have
• Not cartoonish

```html
<!DOCTYPE html>
<html lang="en">
<head>
<meta charset="utf-8">
<title>Harbor Vane Consulting — Business Card</title>
<link rel="stylesheet" href="https://fonts.googleapis.com/css2?family=Michroma&display=swap">
<style>
  :root {
    --stage: #3b3c3e;
    --stage-dark: #252627;
    --stage-light: #47484a;
    --band: #000000;
    --card: #08080a;
    --card-mid: #141416;
    --card-light: #26272a;
    --ink: #ffffff;
    --ink-soft: #cfcfd1;
    --ink-muted: #a9a9ab;
  }
  * { margin: 0; padding: 0; box-sizing: border-box; }
  html, body {
    width: 1200px;
    height: 1200px;
    overflow: hidden;
    background: var(--stage);
    font-family: "Michroma", "Eurostile", sans-serif;
  }
  .canvas {
    position: relative;
    width: 1200px;
    height: 1200px;
  }
  .stage {
    position: absolute;
    inset: 0 0 300px 0;
    background: linear-gradient(160deg, var(--stage-dark) 0%, var(--stage) 55%, var(--stage-light) 100%);
  }
  .business-card {
    position: absolute;
    left: 220px;
    top: 233px;
    width: 760px;
    height: 434px;
    background: var(--card);
    border-radius: 3px;
    overflow: hidden;
    box-shadow: 0 24px 50px rgba(0,0,0,0.5);
    color: var(--ink);
  }
  .card-texture {
    position: absolute;
    inset: 0;
    background:
      radial-gradient(ellipse 38% 48% at 20% 62%, rgba(120,120,124,0.30), transparent 72%),
      radial-gradient(ellipse 26% 32% at 55% 30%, rgba(95,95,100,0.24), transparent 72%),
      radial-gradient(ellipse 20% 26% at 42% 80%, rgba(80,80,84,0.22), transparent 72%),
      linear-gradient(100deg, var(--card-light) 0%, var(--card-mid) 45%, var(--card) 80%);
  }
  .card-sheen {
    position: absolute;
    inset: 0;
    background: linear-gradient(180deg, rgba(255,255,255,0.04) 0%, transparent 40%, rgba(0,0,0,0.25) 100%);
  }
  .brand {
    position: absolute;
    left: 362px;
    top: 86px;
    display: flex;
    align-items: center;
    gap: 10px;
    font-size: 13px;
    letter-spacing: 0.3em;
    white-space: nowrap;
  }
  .brand-square {
    width: 18px;
    height: 18px;
    background: var(--ink);
  }
  .holder-name {
    position: absolute;
    left: 240px;
    top: 165px;
    font-size: 34px;
    font-weight: 400;
    letter-spacing: 0.55em;
    white-space: nowrap;
  }
  .holder-title {
    position: absolute;
    left: 300px;
    top: 224px;
    font-size: 12px;
    letter-spacing: 0.95em;
    color: var(--ink-soft);
    white-space: nowrap;
  }
  .holder-phone {
    position: absolute;
    left: 270px;
    top: 262px;
    font-size: 15px;
    letter-spacing: 0.45em;
    white-space: nowrap;
  }
  .holder-url {
    position: absolute;
    left: 240px;
    top: 360px;
    font-size: 8px;
    letter-spacing: 0.5em;
    color: var(--ink-muted);
    white-space: nowrap;
  }
  .signature-band {
    position: absolute;
    left: 0;
    right: 0;
    bottom: 0;
    height: 300px;
    background: var(--band);
    display: flex;
    align-items: center;
    justify-content: center;
  }
  .signature-name {
    color: var(--ink);
    font-size: 58px;
    letter-spacing: 0.04em;
    white-space: nowrap;
  }
</style>
</head>
<body>
  <main class="canvas">
    <section class="stage">
      <article class="business-card">
        <div class="card-texture" role="img" aria-label="Dark greyscale textured card surface with soft grey highlights"></div>
        <div class="card-sheen"></div>
        <div class="brand"><span class="brand-square"></span><span>HARBOR VANE</span></div>
        <h1 class="holder-name">JOHN DOE</h1>
        <p class="holder-title">DIRECTORS</p>
        <p class="holder-phone">D:555.203.8146</p>
        <p class="holder-url">www.harborvaneconsulting.example</p>
      </article>
    </section>
    <footer class="signature-band">
      <span class="signature-name">HARBOR VANE</span>
    </footer>
  </main>
</body>
</html>
```